Album Jacket for young indie musicians for AFRICA #1 KOLIDONE

We are ORBEL SOUND (orbel-sound.example), a music label for young African musicians living in a slum. I would like to ask you to design our new album's cover jacket. The title is KOLIDONE, musician name is Beluno. Add our label logo (we have various versions and can provide). I attached Beluno's photo also. Please listen to the music of the album on Tunefold. https://tunefold.example/tags/beluno

Our another musician, Rolfe was on the stage of Kenyan most popular TV program yesterday. His music video is so nice. If you have a time, please look at it. https://www.vidlark.example/watch?v=Qx7Rp2Lm9Dz&feature=share

Target Market(s)

International. not only African funs.

Font styles to use
Decorative

Requirements
Must have
• Title, Musician's name, ORBEL SOUND Logo

```html
<!DOCTYPE html>
<html lang="en">
<head>
<meta charset="utf-8">
<title>KOLIDONE — beluno</title>
<link rel="stylesheet" href="https://fonts.googleapis.com/css2?family=Poiret+One&family=EB+Garamond:wght@400&family=Montserrat:wght@800&display=swap">
<style>
  :root {
    --backdrop: #efe6e4;
    --cover: #f4f0ef;
    --ink-rust: #8a4636;
    --label-ink: #4a4443;
    --tone-teal: #1fbfb0;
    --tone-ochre: #e09a3a;
    --tone-rust: #c8452a;
    --tone-sage: #c6d38f;
  }
  * { margin: 0; padding: 0; box-sizing: border-box; }
  html, body {
    width: 1200px;
    height: 1000px;
    overflow: hidden;
    background: var(--backdrop);
  }
  .album-cover {
    position: absolute;
    left: 317px;
    top: 217px;
    width: 567px;
    height: 567px;
    background: var(--cover);
  }
  .label-mark {
    position: absolute;
    left: 14px;
    top: 20px;
    display: flex;
    align-items: center;
    gap: 6px;
  }
  .label-mark__square {
    width: 14px;
    height: 14px;
    background: var(--label-ink);
  }
  .label-mark__name {
    font-family: "Montserrat", sans-serif;
    font-weight: 800;
    font-size: 15px;
    letter-spacing: 0.2px;
    color: var(--label-ink);
  }
  .cover-artwork {
    position: absolute;
    left: 204px;
    top: 58px;
    width: 160px;
    height: 352px;
    background: linear-gradient(180deg,
      var(--tone-rust) 0%,
      var(--tone-ochre) 35%,
      var(--tone-sage) 55%,
      var(--tone-teal) 100%);
    opacity: 0.85;
  }
  .album-title {
    position: absolute;
    left: 0;
    width: 100%;
    top: 448px;
    text-align: center;
    font-family: "Poiret One", sans-serif;
    font-size: 44px;
    font-weight: 400;
    letter-spacing: 1px;
    color: var(--ink-rust);
    line-height: 1;
  }
  .artist-name {
    position: absolute;
    left: 0;
    width: 100%;
    top: 497px;
    text-align: center;
    font-family: "EB Garamond", serif;
    font-weight: 400;
    font-size: 26px;
    color: var(--ink-rust);
    line-height: 1;
  }
</style>
</head>
<body>
  <main class="album-cover">
    <div class="label-mark">
      <span class="label-mark__square"></span>
      <span class="label-mark__name">ORBEL SOUND</span>
    </div>

    <div class="cover-artwork" role="img" aria-label="Cover illustration: a tall shield shape filled with colourful African patterns in teal, ochre, rust and sage"></div>

    <h1 class="album-title">KOLIDONE</h1>
    <p class="artist-name">beluno</p>
  </main>
</body>
</html>
```